SUPPLEMENT BOTTLE LABEL: DRUMMOND

We need a NEW FRESH look to her labels. Something contemporary, clean and professional. The colors need to remain the same but everything else can change, even the logo.

THE CURRENT LABEL IS ATTACHED IN PDF FORMAT

Target Market(s)

WOMEN BETWEEN 35-60

Requirements
Must have
• SAME COLORS
• FRESH
• CLEAN

```html
<!DOCTYPE html>
<html lang="en">
<head>
<meta charset="utf-8">
<title>Cleanse Chocolate – Supplement Label</title>
<link rel="stylesheet" href="https://fonts.googleapis.com/css2?family=Poppins:wght@400;600;700&display=swap">
<style>
  :root {
    --page-bg: #ffffff;
    --label-teal: #7fcbd6;
    --label-teal-deep: #6fc1cd;
    --brand-teal: #6cc3cf;
    --flavor-brown: #b4651b;
    --dot-red: #e0585b;
    --text-white: #ffffff;
    --notice-ink: #3b4a4d;
    --panel-white: #ffffff;
  }
  * { box-sizing: border-box; margin: 0; padding: 0; }
  html, body {
    width: 1200px;
    height: 1000px;
    overflow: hidden;
    background: var(--page-bg);
    font-family: "Poppins", sans-serif;
  }
  .canvas {
    position: relative;
    width: 1200px;
    height: 1000px;
  }
  .label {
    position: absolute;
    left: 300px;
    top: 110px;
    width: 600px;
    height: 780px;
    background: linear-gradient(90deg, var(--label-teal-deep) 0%, var(--label-teal) 30%, var(--label-teal) 70%, var(--label-teal-deep) 100%);
  }
  .brand-panel {
    position: absolute;
    left: 70px;
    top: 40px;
    width: 460px;
    height: 140px;
    background: var(--panel-white);
    display: flex;
    flex-direction: column;
    align-items: center;
    justify-content: center;
    gap: 18px;
  }
  .brand-name {
    font-weight: 400;
    font-size: 40px;
    color: var(--brand-teal);
    letter-spacing: 1px;
  }
  .brand-rule { display: block; }
  .flavor-title {
    position: absolute;
    left: 62px;
    top: 330px;
    font-weight: 700;
    font-size: 52px;
    line-height: 1.12;
    color: var(--flavor-brown);
    letter-spacing: 0.5px;
  }
  .flavor-note {
    position: absolute;
    left: 64px;
    top: 460px;
    font-size: 15px;
    color: var(--text-white);
  }
  .product-type {
    position: absolute;
    left: 64px;
    top: 530px;
    font-weight: 600;
    font-size: 20px;
    line-height: 1.5;
    color: var(--text-white);
  }
  .notice {
    position: absolute;
    left: 0;
    width: 100%;
    top: 680px;
    text-align: center;
    font-size: 12px;
    line-height: 1.45;
    color: var(--notice-ink);
  }
  .net-weight {
    position: absolute;
    left: 0;
    width: 100%;
    top: 736px;
    text-align: center;
    font-size: 17px;
    color: var(--notice-ink);
  }
</style>
</head>
<body>
<main class="canvas">
  <section class="label">
    <header class="brand-panel">
      <span class="brand-name">Bright Renew</span>
      <svg class="brand-rule" width="380" height="6" viewBox="0 0 380 6" aria-hidden="true">
        <line x1="3" y1="3" x2="377" y2="3" stroke="var(--dot-red)" stroke-width="4" stroke-linecap="round" stroke-dasharray="0 9"/>
      </svg>
    </header>

    <h1 class="flavor-title">CLEANSE<br>CHOCOLATE</h1>
    <p class="flavor-note">with other natural flavors</p>

    <p class="product-type">Collagen, Multivitamin, Mineral &amp;<br>Herbal Dietary Supplement Powder</p>

    <p class="notice">Notice: Use this product as a food supplement only.<br>Do not use for weight reduction</p>
    <p class="net-weight">Net WT. 1.21 LBS (551.2 G)</p>
  </section>
</main>
</body>
</html>
```